Evaporative Air Conditioning Summer Service

Would like to design a flyer to send out in an email to existing clients to promote a Pre-summer service for Evaporative Air Conditioners
Cost will be $110.00 inc gst
Tasks included in service are
- Inspection and clean of pads
- Inspection and check float valve, water pump, fan, motor, bearings, drain
- Clean basin
- Supply of bacterial tablet
- Inspect overall condition of unit
- Any repairs if required will be quoted
Please see files attached of a previous very basic flyer I have used for installation and replacement unit costs. This has current contact information
Have also uploaded company logo for use.
Thanks

```html
<!DOCTYPE html>
<html lang="en">
<head>
<meta charset="utf-8">
<title>Evaporative Air Conditioning Summer Service</title>
<link href="https://fonts.googleapis.com/css2?family=Montserrat:wght@500;600;700;800;900&family=Roboto:wght@400;500;700&display=swap" rel="stylesheet">
<style>
  :root {
    --navy: #26409a;
    --royal: #1f4fa8;
    --yellow: #fdd10d;
    --orange: #f58220;
    --charcoal: #3a3a3a;
    --pill: #4b4b4d;
    --white: #ffffff;
    --page: #ffffff;
  }
  * { margin: 0; padding: 0; box-sizing: border-box; }
  html, body { width: 1200px; height: 1200px; overflow: hidden; background: var(--page); }
  .flyer {
    position: absolute; left: 190px; top: 20px;
    width: 820px; height: 1160px; overflow: hidden;
    background: var(--white);
    font-family: "Roboto", Arial, sans-serif;
  }
  .backdrop { position: absolute; inset: 0; }
  .brand {
    position: absolute; left: 420px; top: 72px;
    display: flex; align-items: center; gap: 14px;
    font-family: "Montserrat", sans-serif; font-weight: 800;
    color: var(--royal); font-size: 40px; line-height: 1; letter-spacing: -0.5px;
  }
  .brand-dot { width: 40px; height: 40px; border-radius: 50%; background: var(--orange); }
  .brand-name small { display: block; font-size: 19px; letter-spacing: 2px; margin-top: 6px; }
  .hero {
    position: absolute; left: 40px; top: 196px; width: 740px; height: 270px;
    background: linear-gradient(100deg, #8a98a6 0%, #e9ecef 32%, #6a6c70 52%, #f2f2f2 72%, #f7b23a 100%);
    border-radius: 6px;
  }
  .price-badge {
    position: absolute; left: 45px; top: 567px; width: 309px; height: 310px;
    border-radius: 38px;
    background: linear-gradient(100deg, var(--yellow) 30%, var(--orange) 100%);
    color: var(--navy); font-family: "Montserrat", sans-serif; font-weight: 900;
    text-align: center;
  }
  .price-badge::before {
    content: ""; position: absolute; inset: 11px;
    border: 1.5px dashed var(--navy); border-radius: 30px;
  }
  .price-line { position: absolute; left: 0; width: 100%; line-height: 1; white-space: nowrap; }
  .price-cost { top: 16px; font-size: 90px; letter-spacing: -1px; }
  .price-will { top: 111px; font-size: 54px; }
  .price-amount { top: 167px; font-size: 68px; letter-spacing: -2.5px; }
  .price-gst { top: 239px; font-size: 48px; }
  .tasks { position: absolute; left: 415px; top: 588px; width: 400px; color: var(--white); }
  .tasks-title { color: var(--orange); font-weight: 700; font-size: 27px; line-height: 30px; margin-bottom: 7px; }
  .task-list { list-style: none; }
  .task-list li {
    position: relative; padding-left: 25px; font-size: 22px; line-height: 26px; margin-bottom: 7px;
  }
  .task-list .tick { position: absolute; left: 0; top: 5px; width: 17px; height: 17px; }
  .task-list .tight { font-size: 20.5px; letter-spacing: -0.7px; white-space: nowrap; }
  .contact-pill {
    position: absolute; left: 247px; top: 915px; width: 310px; height: 52px;
    background: var(--pill); border-radius: 26px;
    color: var(--orange); font-weight: 700; font-size: 34px;
    display: flex; align-items: center; justify-content: center;
  }
  .contact { position: absolute; left: 0; width: 820px; text-align: center; line-height: 1; }
  .contact-phone {
    top: 976px; font-family: "Montserrat", sans-serif; font-weight: 800;
    font-size: 72px; color: var(--charcoal); letter-spacing: -1px;
  }
  .contact-email {
    top: 1045px; font-family: "Montserrat", sans-serif; font-weight: 700;
    font-size: 17px; color: var(--charcoal);
  }
  .contact-abn {
    top: 1069px; font-family: "Montserrat", sans-serif; font-weight: 800;
    font-size: 32px; color: var(--white);
  }
  .footnote {
    top: 1114px; font-family: "Montserrat", sans-serif; font-weight: 500;
    font-size: 11.5px; color: var(--navy);
  }
</style>
</head>
<body>
<main class="flyer">
  <svg class="backdrop" width="820" height="1160" viewBox="0 0 820 1160" aria-hidden="true">
    <defs>
      <linearGradient id="footerFill" x1="0" y1="0" x2="1" y2="0">
        <stop offset="0.35" stop-color="#fdd10d"/>
        <stop offset="1" stop-color="#f58220"/>
      </linearGradient>
    </defs>
    <path d="M0 500 Q320 455 820 472 L820 940 L0 940 Z" fill="url(#footerFill)"/>
    <path d="M0 525 Q320 480 820 500 L820 933 L0 933 Z" fill="#26409a"/>
    <rect x="0" y="933" width="820" height="227" fill="url(#footerFill)"/>
  </svg>

  <div class="brand">
    <span class="brand-dot"></span>
    <span class="brand-name">SUMMIT<small>GAS &amp; PLUMBING</small></span>
  </div>

  <div class="hero" role="img" aria-label="Photo of a technician fitting a wall-mounted water heater beside an outdoor air conditioning unit and a split system head unit, with flowing orange waves behind"></div>

  <div class="price-badge">
    <div class="price-line price-cost">COST</div>
    <div class="price-line price-will">WILL BE</div>
    <div class="price-line price-amount">$110.00</div>
    <div class="price-line price-gst">INC GST</div>
  </div>

  <section class="tasks">
    <h2 class="tasks-title">Tasks included in service are</h2>
    <ul class="task-list">
      <li><svg class="tick" viewBox="0 0 16 16"><path d="M2 9 L6 13 L14 2" fill="none" stroke="#fff" stroke-width="1.8"/></svg>Inspection and clean of pads</li>
      <li><svg class="tick" viewBox="0 0 16 16"><path d="M2 9 L6 13 L14 2" fill="none" stroke="#fff" stroke-width="1.8"/></svg>Inspection and check float valve,<br><span class="tight">water pump, fan, motor, bearings, drain</span></li>
      <li><svg class="tick" viewBox="0 0 16 16"><path d="M2 9 L6 13 L14 2" fill="none" stroke="#fff" stroke-width="1.8"/></svg>Clean basin</li>
      <li><svg class="tick" viewBox="0 0 16 16"><path d="M2 9 L6 13 L14 2" fill="none" stroke="#fff" stroke-width="1.8"/></svg>Supply of bacterial tablet</li>
      <li><svg class="tick" viewBox="0 0 16 16"><path d="M2 9 L6 13 L14 2" fill="none" stroke="#fff" stroke-width="1.8"/></svg>Inspect overall condition of unit</li>
      <li><svg class="tick" viewBox="0 0 16 16"><path d="M2 9 L6 13 L14 2" fill="none" stroke="#fff" stroke-width="1.8"/></svg>Any repairs if required will<br>be quoted</li>
    </ul>
  </section>

  <div class="contact-pill">Contract Us</div>
  <div class="contact contact-phone">0491570156</div>
  <div class="contact contact-email">admin@summitgasplumbing.com.au</div>
  <div class="contact contact-abn">ABN 51824753556</div>
  <div class="contact footnote">*If compressor location cannot be back to back with head unit installation cost will be quoted onsite</div>
</main>
</body>
</html>
```